Business branding (card, web design) needed for Remedial / Sports massage

I need a clean, fresh design for my sports massage business called Brightwell-Motion.

I work with high profile professional sports teams (massage, clinical tapeing, health assessments, pilates, coaching) however would like to expand into the entertainment market so need a design that would appeal to both.
NO LOTUS FLOWERS, HANDS OR YOGA POSES FOR DESIGNS

The successful brand design will need to be scalable (e.g. resolution/sizing) to work holistically across my website, marketing collateral and clothing.

Colour pallets that appeal to me - Black, white, blue, green, taupe,
and would prefer clean crisp designs that evoke professionalism, continuous improvement, flow and balance.

Good Luck, can't wait to find my new brand... :)
Updates

I have uploaded a business card that I do like,  See if you can be creative with the logo

Thanks

Target Market(s)

professional sports teams / athletes, and entertainment professionals.

I HAVE UPLOADED A PDF OF WHAT I HAVE DONE. YOU MAY USE LOGO BUT BE CREATIVE PLEASE.

Industry/Entity Type

Entertainment

Contact Information for Business Card

Brightwell-Motion
'Move With Ease' (strap line)

Colette Farrow
Director / Remedial Massage

0417263950
212 Larkmore Street
Kelbridge, VIC 3261

www.brightwell-motion.com.au
info@brightwell-motion.com.au

Logo Text

Brightwell-Motion

Logo styles of interest
Pictorial/Combination Logo
Abstract Logo
Requirements
Should not have
• FLOWERS

```html
<!DOCTYPE html>
<html lang="en">
<head>
<meta charset="utf-8">
<title>Brightwell-Motion Business Card</title>
<link rel="stylesheet" href="https://fonts.googleapis.com/css2?family=Gentium+Book+Plus&family=Tinos&display=swap">
<style>
  :root {
    --page-bg: #f2f2f2;
    --card-bg: #ffffff;
    --card-edge: #c9c9c9;
    --ink: #111111;
    --phone-grey: #666666;
    --brand-green: #5aa832;
    --leaf-cream: #e6e4b4;
    --leaf-yellow: #fdc50e;
    --leaf-orange: #f07a22;
    --leaf-brown: #9a7437;
    --leaf-magenta: #c8205a;
  }
  * { margin: 0; padding: 0; box-sizing: border-box; }
  html, body {
    width: 1200px;
    height: 1082px;
    overflow: hidden;
    background: var(--page-bg);
  }
  .canvas {
    position: relative;
    width: 1200px;
    height: 1082px;
  }
  .card {
    position: absolute;
    top: 389px;
    width: 540px;
    height: 304px;
    overflow: hidden;
  }
  .card--front {
    left: 40px;
    background: var(--card-bg);
    border: 1px solid var(--card-edge);
    color: var(--ink);
  }
  .card--back { left: 620px; }
  .card-text {
    position: absolute;
    line-height: 1;
    white-space: nowrap;
  }
  .holder-name {
    left: 264px; top: 50px;
    font-family: "Gentium Book Plus", serif;
    font-size: 38px;
  }
  .holder-role {
    left: 264px; top: 92px;
    font-family: "Tinos", serif;
    font-size: 16px;
  }
  .contact-phone {
    left: 264px; top: 186px;
    font-family: "Tinos", serif;
    font-size: 42px;
    color: var(--phone-grey);
    letter-spacing: 1px;
  }
  .contact-email, .contact-web {
    left: 264px;
    font-family: "Tinos", serif;
    font-size: 19px;
  }
  .contact-email { top: 234px; }
  .contact-web { top: 260px; }
  .brand-dot {
    position: absolute;
    left: 66px; top: 132px;
    width: 38px; height: 38px;
    border-radius: 50%;
    background: var(--brand-green);
  }
  .brand-name {
    left: 24px; top: 184px;
    font-family: "Gentium Book Plus", serif;
    font-size: 22px;
  }
  .brand-tagline {
    left: 26px; top: 212px;
    font-family: "Tinos", serif;
    font-size: 14px;
    letter-spacing: 2.2px;
  }
  .studio-address {
    left: 26px;
    font-family: "Tinos", serif;
    font-size: 15px;
  }
  .studio-address--street { top: 245px; }
  .studio-address--town { top: 264px; }
  .leaf-pattern {
    display: block;
    width: 540px;
    height: 304px;
  }
</style>
</head>
<body>
  <main class="canvas">
    <section class="card card--front">
      <span class="card-text holder-name">Colette Farrow</span>
      <span class="card-text holder-role">Remedial Massage Therapist</span>

      <span class="brand-dot"></span>
      <span class="card-text brand-name">Brightwell-Motion</span>
      <span class="card-text brand-tagline">Move With Ease</span>
      <span class="card-text studio-address studio-address--street">212 Larkmore Street</span>
      <span class="card-text studio-address studio-address--town">Kelbridge, Vic 3261</span>

      <span class="card-text contact-phone">0417263950</span>
      <span class="card-text contact-email">info@brightwell-motion.com.au</span>
      <span class="card-text contact-web">www.brightwell-motion.com.au</span>
    </section>

    <section class="card card--back">
      <svg class="leaf-pattern" viewBox="0 0 540 304" role="img" aria-label="Illustrated pattern of overlapping outlined leaves in cream, yellow, orange, brown and magenta">
        <defs>
          <linearGradient id="leafTones" x1="0" y1="0" x2="1" y2="1">
            <stop offset="0" stop-color="#e6e4b4"/>
            <stop offset="0.4" stop-color="#fdc50e"/>
            <stop offset="0.65" stop-color="#f07a22"/>
            <stop offset="0.85" stop-color="#9a7437"/>
            <stop offset="1" stop-color="#c8205a"/>
          </linearGradient>
        </defs>
        <rect width="540" height="304" fill="url(#leafTones)"/>
      </svg>
    </section>
  </main>
</body>
</html>
```